Civic Counsel and Advocacy Network needs poster design for landlord/tenant cases

We're seeking a poster design (11x17) to spread awareness for services by "Civic Counsel and Advocacy Network". The services they're trying to communicate are regarding housing/landlord/tenant matters.

We'd like the poster to (1) reflect the color scheme and branding of their website www.ccanmorvale.org, (2) contain the following copy: "Everyone needs safe and suitable housing, whether they own a home or rent one. When homelessness threatens, we at CCN help clients free of charge through eviction diversion programs and mortgage/tax foreclosure prevention.", and (3) contain their contact information:

Civic Counsel and Advocacy Network, Inc.
"We are YOUR Law Firm for Housing matters"
Contact us at: (555) 314-2869
housing @ccanmorvale.org
www.ccanmorvale.org

Target Market(s)

People who may be facing eviction or homelessness

Industry/Entity Type

Legal

Colors
0054AA
0677BA
7BADD7
CADEEF
E8F1F8
FFC000
F8CF3A
FAE287
FDF2CF
FEFAEE
EB3D1F
EC4F4E
F09395
F8D3D4
FCEDEE

Requirements
Must have
• Must include colors from website: https://ccanmorvale.org/

```html
<!DOCTYPE html>
<html lang="en">
<head>
<meta charset="UTF-8">
<title>Civic Counsel and Advocacy Network – Housing Poster</title>
<link rel="stylesheet" href="https://fonts.googleapis.com/css2?family=Noto+Serif:wght@400;700;800&family=Poppins:wght@400;500;700&display=swap">
<style>
  :root {
    --red: #df4935;
    --red-dark: #c73c2a;
    --navy: #2b3f8e;
    --navy-deep: #233479;
    --white: #ffffff;
    --ink: #1d1d1f;
    --grey: #9a9a9a;
  }
  * { margin: 0; padding: 0; box-sizing: border-box; }
  html, body { width: 696px; height: 1200px; overflow: hidden; background: #fff; }
  .poster {
    position: relative; width: 696px; height: 1200px; overflow: hidden;
    background: linear-gradient(180deg, var(--red) 0%, var(--red-dark) 45%, var(--red) 100%);
    font-family: "Poppins", sans-serif; color: var(--white);
  }
  .abs { position: absolute; }

  /* brand */
  .brand { top: 40px; left: 0; width: 100%; display: flex; justify-content: center; align-items: center; gap: 12px; }
  .brand-mark { width: 60px; height: 60px; border-radius: 50%; border: 3px solid var(--white); }
  .brand-name { font-family: "Noto Serif", serif; font-weight: 700; font-size: 15px; line-height: 1.15; color: var(--white); text-transform: uppercase; letter-spacing: .5px; }

  .org-line { top: 138px; width: 100%; text-align: center; font-family: "Noto Serif", serif; font-size: 19px; letter-spacing: 3.5px; text-transform: uppercase; }

  .headline { width: 100%; text-align: center; font-family: "Noto Serif", serif; text-transform: uppercase; }
  .hl-needs { top: 180px; font-size: 38px; font-weight: 400; display: flex; justify-content: center; align-items: center; gap: 8px; }
  .hl-needs::before, .hl-needs::after { content: ""; width: 72px; height: 2px; background: var(--white); }
  .hl-safe { top: 230px; font-size: 50px; font-weight: 700; letter-spacing: -.5px; }
  .hl-housing { top: 276px; font-size: 118px; font-weight: 800; color: var(--navy); letter-spacing: -4px; line-height: 1.05; }
  .hl-whether { top: 388px; width: 100%; text-align: center; font-size: 38px; font-weight: 400; text-transform: uppercase; }
  .hl-box { top: 443px; left: 80px; width: 528px; height: 56px; background: var(--navy); border-radius: 6px;
    text-align: center; font-size: 40px; font-weight: 700; line-height: 56px; text-transform: uppercase; }

  .blue-band { top: 0; left: 0; }

  .photo-house { top: 572px; left: 0; width: 440px; height: 456px;
    background: linear-gradient(160deg, #e7e8ea 0%, #cfd3d8 45%, #9ba1a8 75%, #5f6a5a 100%); }

  .threat { top: 600px; right: 88px; text-align: right; text-transform: uppercase; font-size: 23px; line-height: 1.0; }
  .threat strong { font-weight: 700; display: block; }
  .dots { top: 690px; right: 88px; display: flex; gap: 3px; }
  .dots span { width: 5px; height: 5px; border-radius: 50%; background: #6b79b4; }
  .dots span:last-child { background: var(--red); }
  .threat-body { top: 706px; right: 88px; text-align: right; font-size: 13.5px; line-height: 1.3; }

  /* footer */
  .motto { top: 1074px; left: 80px; font-family: "Noto Serif", serif; font-size: 28px; line-height: 24px; text-transform: uppercase; color: var(--ink); letter-spacing: -.5px; }
  .motto .m-navy { color: var(--navy); font-weight: 700; }
  .motto .m-red { color: var(--red); font-weight: 700; }
  .divider { top: 1065px; left: 333px; height: 118px; border-left: 1.5px dashed var(--grey); }
  .contact-org { top: 1094px; left: 357px; font-size: 11.5px; font-weight: 700; color: var(--ink); text-transform: uppercase; }
  .contact-line { top: 1120px; left: 357px; font-size: 11px; color: var(--ink); display: flex; align-items: center; gap: 4px; }
  .contact-line .gap { width: 10px; }
  .web-pill { top: 1144px; left: 360px; width: 248px; height: 22px; border-radius: 11px; background: var(--red);
    text-align: center; font-size: 13.5px; letter-spacing: 3px; line-height: 22px; color: var(--white); }
</style>
</head>
<body>
<main class="poster">

  <header class="abs brand">
    <div class="brand-mark"></div>
    <div class="brand-name">Civic Counsel and<br>Advocacy Network</div>
  </header>

  <p class="abs org-line">Civic Counsel and Advocacy Network</p>

  <h1>
    <span class="abs headline hl-needs">Everyone needs</span>
    <span class="abs headline hl-safe">Safe and suitable</span>
    <span class="abs headline hl-housing">Housing</span>
    <span class="abs hl-whether">Whether they own</span>
    <span class="abs hl-box">A home or rent one</span>
  </h1>
  <svg class="abs" style="top:496px;left:80px" width="22" height="22" viewBox="0 0 22 22"><path d="M0 0 H22 L2 20 Z" fill="var(--navy)"/></svg>

  <svg class="abs blue-band" width="696" height="1200" viewBox="0 0 696 1200">
    <path fill="var(--navy)" d="M0 560 L20 552 L40 566 L62 548 L84 562 L110 545 L130 560 L152 540 L176 556 L198 546 L222 563 L246 549 L270 558 L292 540 L318 557 L340 547 L364 562 L388 544 L410 558 L436 548 L460 564 L484 546 L508 556 L530 542 L556 560 L580 548 L604 562 L628 545 L652 557 L676 546 L696 554 L696 1040 L0 1040 Z"/>
  </svg>

  <div class="abs photo-house" role="img" aria-label="Photograph of a modern white two-storey house with a dark roof, balcony and garage"></div>

  <svg class="abs" style="top:1010px;left:0" width="696" height="190" viewBox="0 0 696 190">
    <path fill="var(--white)" d="M0 18 L24 10 L48 22 L70 6 L96 20 L120 12 L146 26 L170 8 L196 22 L220 14 L246 28 L270 10 L296 24 L320 14 L346 30 L372 16 L398 28 L424 18 L450 32 L476 20 L502 34 L528 22 L556 36 L582 24 L610 38 L636 26 L664 40 L696 30 L696 190 L0 190 Z"/>
  </svg>

  <section>
    <p class="abs threat">When<br>homelessness<strong>threatens</strong></p>
    <div class="abs dots"><span></span><span></span><span></span></div>
    <p class="abs threat-body">we at CCN help clients<br>free of charge through<br>eviction diversion<br>programs and mort-<br>gage/tax foreclosure<br>prevention</p>
  </section>

  <footer>
    <p class="abs motto">We are<br>your law firm<br><span class="m-navy">for housing</span><br><span class="m-red">matters</span></p>
    <div class="abs divider"></div>
    <p class="abs contact-org">Civic Counsel and Advocacy Network, Inc</p>
    <p class="abs contact-line">
      <svg width="10" height="10" viewBox="0 0 24 24"><path fill="var(--red)" d="M6.6 10.8a15 15 0 0 0 6.6 6.6l2.2-2.2c.3-.3.7-.4 1-.2 1.1.4 2.3.6 3.6.6.6 0 1 .4 1 1V20c0 .6-.4 1-1 1A17 17 0 0 1 3 4c0-.6.4-1 1-1h3.5c.6 0 1 .4 1 1 0 1.3.2 2.5.6 3.6.1.3 0 .7-.2 1z"/></svg>
      <strong>(555) 314-2869</strong>
      <span class="gap"></span>
      <svg width="11" height="8" viewBox="0 0 22 16"><rect width="22" height="16" rx="1" fill="var(--red)"/><path d="M1 1 L11 9 L21 1" stroke="#fff" stroke-width="2" fill="none"/></svg>
      housing @ccanmorvale.org
    </p>
    <p class="abs web-pill">www.ccanmorvale.org</p>
  </footer>

</main>
</body>
</html>
```